Flyer-Design für Bücherei
Zielgruppe
Wir sind eine ehrenamtlich geführte Bücherei in Wendelsau. Wir bieten unseren Kunden eine professionell geführte Bücherei im moderne Stil mit mind. 30 neuen Medien pro Woche. Unsere Zielgruppe sind die Bewohner in Wendelsau, vor allen Kinder, Familien mit Kindern und Senioren.
Wir haben über 12.000 Medien, bestehend aus Bilderbücher, Kinderbücher, Jugendliteratur, Romane, Hörbücher für Kinder, Hörlinos, Reiseführer, Zeitschriften, Spiele und Sachliteratur für Kinder und Jugendliche. Wir haben einen online Katalog und unsere Kunden können online ihre ausgeliehen Medien sehen und verlängern, sowie Vormerkungen platzieren.
Neben den Büchereibetrieb bieten wir Regelmäßige Autorenlesungen, Vorleseaktionen für Kinder, Bastelabende und Führungen für Schul- und Kindergartengruppen.
Ziele des Fördervereins sind:
- Die Bücherei als Kultur-, Bildungs- und Freizeiteinrichtung unterstützen und erhalten
- Durch Öffentlichkeitsarbeit die Bücherei stärker im Bewusstsein der Bevölkerung verankern
- Maßnahmen zur Verbesserung der Leistungsfähigkeit und Attraktivität der Bücherei ergreifen
- Veranstaltung fördern und organisieren
- Neue Freunde und Förderer für die Bücherei gewinnen
Aufgabenstellung
Öffnungszeiten:
Montag, Donnerstag, Freitag 15:00 - 18:00
Kontaktdaten:
Telefon: 07158-63-907
E-Mail: info@buecherei-wendelsau.de
Online-Katalog: online.buecherei-wendelsau.de
Das Design soll schön und ansprechend sein. Es soll ein zwei mal gefalzter Flyer im Din lang Format sein. Wenn er zusammengefaltet ist soll es eine Startseite geben wo Förderverein der Bücherei Wendelsau e.V. drauf steht und auf der Rückseite die Öffnungszeiten und Kontaktdaten.
Bitte formulieren Sie gerne die Texte um, so das die Texte zum Design des Flyers passen . Wir sind eine moderne und aktuelle Bücherei und wollen so auch im Flyer auftreten. Aktuell haben wir nur die Akzentfarbe Rot ansonsten sind wir bei Schwarz und Weiß, wie sie auch im Logo sehen.
Wenn der Flyer uns überzeugt, sind wir gewillt auch noch zwei Roll-Ups designen zu lassen, sowie in Zukunft mit ihnen weiter zusammen zuarbeiten.

```html
<!DOCTYPE html>
<html lang="de">
<head>
<meta charset="utf-8">
<title>Flyer Bücherei Wendelsau</title>
<link rel="stylesheet" href="https://fonts.googleapis.com/css2?family=Crimson+Pro:wght@400;500&family=Montserrat:wght@700&display=swap">
<style>
  :root {
    --red: #d0121b;
    --ink: #3c3c3c;
    --paper: #e4e3e3;
    --frame: #a2a2a2;
    --black: #141414;
  }
  * { margin: 0; padding: 0; box-sizing: border-box; }
  html, body { width: 847px; height: 1200px; overflow: hidden; background: var(--frame); }
  body { position: relative; font-family: "Crimson Pro", Georgia, serif; color: var(--ink); font-variant-numeric: oldstyle-nums; }
  .panel { position: absolute; left: 15px; width: 818px; background: var(--paper); overflow: hidden; }
  .panel--outside { top: 22px; height: 577px; }
  .panel--inside { top: 607px; height: 577px; }
  .abs { position: absolute; }
  .heading { color: var(--red); font-weight: 400; line-height: 1; }
  .heading--xl { font-size: 29px; }
  .body-text { font-size: 11.5px; line-height: 16.5px; }
  .goals { list-style: none; left: 32px; top: 208px; width: 240px; font-size: 11.3px; line-height: 14px; }
  .goals li { padding-left: 17px; text-indent: -17px; margin-bottom: 7.5px; }
  .goals li::before { content: "- "; }
  .photo { position: absolute; }
  .photo--cover { left: 554px; top: 0; width: 264px; height: 577px;
    background: linear-gradient(160deg, #b88a3c 0%, #5f7a2c 30%, #8aa548 55%, #2c2a30 75%, #1e1e26 100%); }
  .brand { left: 576px; top: 44px; width: 242px; height: 67px; background: rgba(240,238,234,0.82);
    display: flex; align-items: center; justify-content: flex-end; gap: 10px; padding-right: 12px; }
  .brand__mark { width: 28px; height: 28px; background: var(--red); }
  .brand__name { font-family: "Crimson Pro", Georgia, serif; font-weight: 500; font-size: 21px; line-height: 21px; color: var(--black); text-align: right; }
  .media-label { font-size: 11.3px; line-height: 13px; color: var(--ink); }
  .photo--stacks { left: 445px; top: 190px; width: 373px; height: 170px;
    background: linear-gradient(90deg, #8a7a4c, #5d6a3c 40%, #7a5a38 70%, #9c8c5a); opacity: .85; }
  .photo--group { left: 0; top: 251px; width: 504px; height: 326px;
    background: linear-gradient(180deg, #d9c3a8 0%, #c79a8c 40%, #6d7f9a 75%, #4c5470 100%); }
  .events { right: 13px; top: 415px; width: 300px; text-align: right; }
</style>
</head>
<body>

<section class="panel panel--outside">
  <h2 class="heading heading--xl abs" style="left:32px;top:132px;font-size:28px;line-height:28px;">Ziele des<br>Fördervereins:</h2>
  <ul class="goals abs">
    <li>Die Bücherei als Kultur-, Bildungs- und Freizeit einrichtung unterstützen und erhalten</li>
    <li>Durch Öffentlichkeitsarbeit die Bücherei stärker im Bewusstsein der Bevölkerung verankern</li>
    <li>Maßnahmen zur Verbesserung der Leistungs-fähigkeit und Attraktivität der Bücherei ergreifen</li>
    <li>Veranstaltung fördern und organisieren</li>
    <li>Neue Freunde und Förderer für die Bücherei gewinnen</li>
  </ul>

  <svg class="abs" style="left:0;top:425px" width="100" height="130" viewBox="0 0 100 130" fill="none" stroke="var(--red)" stroke-width="3.5" stroke-linecap="round" aria-hidden="true">
    <path d="M48 5 A62 62 0 1 0 94 55"/>
    <path d="M40 28 A38 38 0 1 0 77 60"/>
    <circle cx="32" cy="64" r="15"/>
    <path d="M32 64 L82 14"/>
    <path d="M74 8 L80 18 L92 20 L86 9 Z"/>
  </svg>

  <svg class="abs" style="left:403px;top:70px" width="118" height="102" viewBox="0 0 118 102" fill="none" stroke="var(--red)" stroke-width="3" stroke-linecap="round" stroke-linejoin="round" aria-hidden="true">
    <path d="M20 2 H96 M20 2 Q12 14 20 26 H96 M20 26 Q12 38 20 50 M2 28 H74 M2 28 Q-4 40 2 52 H70 M12 52 Q4 64 12 76 H66"/>
    <path d="M36 2 V26 L42 20 L48 26 V2"/>
    <path d="M60 14 H70 M78 14 H84 M30 64 H44"/>
    <path d="M70 54 L90 100 L94 84 L110 96 L114 90 L98 78 L112 72 Z"/>
    <path d="M88 42 L84 50 M100 46 L94 52 M104 58 L96 60"/>
  </svg>

  <h2 class="heading heading--xl abs" style="left:310px;top:193px;">Online-Katalog</h2>
  <p class="body-text abs" style="left:310px;top:234px;width:240px;">Sie können Ihre ausgeliehen Medien online sehen und verlängern, sowie Vormerkungen platzieren.</p>

  <h2 class="heading heading--xl abs" style="left:310px;top:358px;">Öffnungszeiten</h2>
  <p class="body-text abs" style="left:310px;top:400px;">Montag, Donnerstag, Freitag:<span style="margin-left:18px">15:00 - 18:00</span></p>

  <h2 class="heading heading--xl abs" style="left:310px;top:446px;">Kontakt</h2>
  <p class="body-text abs" style="left:310px;top:487px;">Telefon: 07158-63-907<br>E-Mail: info@buecherei-wendelsau.de<br>Online-Katalog: online.buecherei-wendelsau.de</p>

  <div class="photo photo--cover" role="img" aria-label="Foto: Junge im Anzug liest im Herbstpark ein rotes Buch"></div>
  <div class="brand abs">
    <span class="brand__mark"></span>
    <span class="brand__name">BÜCHEREI<br>WENDELSAU</span>
  </div>
</section>

<section class="panel panel--inside">
  <svg class="abs" style="left:0;top:0" width="440" height="240" viewBox="0 0 440 240" fill="none" stroke="var(--red)" stroke-width="2.5" stroke-linejoin="round" aria-hidden="true">
    <!-- Bilderbücher -->
    <path d="M43 40 H89 V75 H43 Z M46 40 Q66 34 66 44 Q66 34 86 40 M46 40 V70 H86 V40"/>
    <!-- Spiele und Sachliteratur -->
    <rect x="158" y="21" width="48" height="38"/>
    <path d="M164 27 H200 V53 H164 Z"/>
    <text x="182" y="46" font-family="Montserrat, sans-serif" font-size="14" fill="var(--red)" stroke="none" text-anchor="middle">A-Z</text>
    <!-- Zeitschriften -->
    <path d="M272 28 V60 Q286 56 296 62 Q306 56 320 60 V28 M276 24 Q288 22 296 30 V60 M316 24 Q304 22 296 30"/>
    <!-- Reiseführer -->
    <path d="M359 35 H373 V77 H359 Z M373 39 H387 V77 H373 Z M387 33 H407 V77 H387 Z M366 44 V60 M380 48 H387 M395 50 H407 M395 62 H407"/>
    <!-- Kinderbücher -->
    <path d="M25 120 H61 V165 H25 Z M25 124 H61 M29 120 V165"/>
    <!-- Jugendliteratur -->
    <path d="M122 184 H170 V219 H122 Z M146 184 V219 M128 192 H141 M128 199 H141 M128 206 H141 M128 213 H141 M151 192 H164 M151 199 H164 M151 206 H164 M151 213 H164"/>
    <!-- Romane -->
    <path d="M232 175 H269 V222 H232 Z M238 175 V222 M250 175 V192 L255 187 L260 192 V175"/>
  </svg>

  <svg class="abs" style="left:414px;top:101px" width="28" height="52" viewBox="0 0 28 52" fill="none" stroke="var(--red)" stroke-width="2.5" stroke-linejoin="round" aria-hidden="true">
    <path d="M3 14 L5 2 L11 10 H17 L23 2 L25 14 Q27 22 24 30 V48 H4 V30 Q1 22 3 14 Z"/>
    <circle cx="10" cy="20" r="2"/><circle cx="18" cy="20" r="2"/>
  </svg>

  <svg class="abs" style="left:320px;top:145px" width="62" height="58" viewBox="0 0 62 58" fill="none" stroke="var(--red)" stroke-width="2.5" stroke-linejoin="round" aria-hidden="true">
    <path d="M6 30 Q6 4 31 4 Q56 4 56 30"/>
    <rect x="2" y="28" width="8" height="16" rx="3"/><rect x="52" y="28" width="8" height="16" rx="3"/>
    <path d="M14 22 Q22 18 31 24 Q40 18 48 22 V52 Q40 48 31 54 Q22 48 14 52 Z M31 24 V54 M19 30 H27 M19 36 H27 M19 42 H27 M35 30 H43 M35 36 H43 M35 42 H43"/>
  </svg>

  <p class="media-label abs" style="left:45px;top:88px;">Bilderbücher</p>
  <p class="media-label abs" style="left:145px;top:66px;">Spiele und Sach-<br>literatur für Kinder<br>und Jugendliche</p>
  <p class="media-label abs" style="left:275px;top:76px;">Zeitschriften</p>
  <p class="media-label abs" style="left:355px;top:94px;">Reiseführer</p>
  <p class="media-label abs" style="left:404px;top:161px;">Hörlinos</p>
  <p class="media-label abs" style="left:27px;top:183px;">Kinderbücher</p>
  <p class="media-label abs" style="left:129px;top:232px;">Jugendliteratur</p>
  <p class="media-label abs" style="left:245px;top:233px;">Romane</p>
  <p class="media-label abs" style="left:319px;top:210px;">Hörbücher für Kinder</p>

  <h2 class="heading abs" style="left:139px;top:125px;font-size:31px;">12.000 Medien</h2>

  <h2 class="heading abs" style="left:533px;top:31px;font-size:29px;line-height:30px;">30 neuen Medien<br>pro Woche</h2>
  <p class="body-text abs" style="left:533px;top:102px;width:272px;text-align:justify;">Wir sind eine ehrenamtlich geführte Bücherei in Wendelsau. Wir bieten Ihnen eine professionell geführte Bücherei im moderne Stil mit mind. 30 neuen Medien pro Woche.</p>

  <div class="photo photo--stacks" role="img" aria-label="Foto: ansteigende Stapel alter Bücher"></div>
  <svg class="abs" style="left:560px;top:170px" width="170" height="70" viewBox="0 0 170 70" aria-hidden="true">
    <path d="M4 62 Q70 56 140 14" fill="none" stroke="var(--red)" stroke-width="8" stroke-linecap="round"/>
    <path d="M128 6 L166 2 L148 34 Z" fill="var(--red)"/>
  </svg>

  <div class="photo photo--group" role="img" aria-label="Foto: Vorleserin mit einer Gruppe Kinder, die sich melden"></div>

  <div class="events abs">
    <h2 class="heading heading--xl">Versanstaltungen</h2>
    <p class="body-text" style="margin-top:18px;">Neben den Büchereibetrieb bieten wir Regelmäßige Autorenlesungen, Vorleseaktionen für Kinder, Bastelabende und Führungen für Schul- und Kindergartengruppen.</p>
  </div>
</section>

</body>
</html>
```